Business Card Design Project

I am a psychotherapist, counselor and expressive arts therapist (means I use every art form imaginable in the service of healing). I'm just starting out in private practice in San Francisco, CA. I work with individual adults, children and families. I'd like the card to mirror the simplicity and color palate of my website. I also would love if there is a symbol, image of fire, flame or spark (that is warming, not frightening).

Check out my website: www.lorabecketmft.com

I want the cards to be printed in letter press so please keep that in mind!

Target Market(s)

Upper Middle Class Adults who are progressively minded, artistic or artists, open to psychotherapy, interested in health & healing.

Industry/Entity Type

Business

Requirements
Must have
• Text to be included:

Lora Becket
Counseling, Psychotherapy & Expressive Arts

2914 Alderwood Avenue, Suite D
San Francisco, CA 94127
p. 415.206.3791
lorajanebecket@meadowpost.net

www.lorabecketmft.com

MFT License Number 48671

It's OK to abbreviate Number to # or Street to St., etc.

Must be compatible with letter press printing.
Nice to have
• I don't have a logo. I don't expect designers to necessarily create one for me, but if someone comes up with a simple image (see above about flame), that would be great. I don't have much of a budget now, but expect that to change in the next year or so and then could buy a logo for my website, future letterhead, etc.

```html
<!DOCTYPE html>
<html lang="en">
<head>
<meta charset="utf-8">
<title>Lora Becket Business Card</title>
<link rel="stylesheet" href="https://fonts.googleapis.com/css2?family=Vollkorn:wght@400;500&family=Open+Sans:wght@400&display=swap">
<style>
  :root {
    --page-bg: #d9d9d9;
    --rose: #dc2f58;
    --rose-light: #ea6a8c;
    --rose-text: #e2446a;
    --charcoal: #2b292a;
    --charcoal-light: #3b393a;
    --white: #ffffff;
    --muted: #e8e6e6;
  }
  * { margin: 0; padding: 0; box-sizing: border-box; }
  html, body { width: 1200px; height: 861px; overflow: hidden; }
  body { background: var(--page-bg); position: relative; }

  .card {
    position: absolute;
    left: 443px; top: 113px;
    width: 321px; height: 559px;
    overflow: hidden;
    background: linear-gradient(160deg, var(--charcoal-light), var(--charcoal) 60%);
  }
  .card__top {
    position: absolute; inset: 0 0 auto 0; height: 260px;
  }
  .card__top svg { display: block; }

  .brand {
    position: absolute; left: 0; width: 321px; top: 40px;
    text-align: center; color: var(--white);
  }
  .brand__mark {
    width: 58px; height: 58px; border-radius: 50%;
    background: var(--white); margin: 12px auto 0;
  }
  .brand__name {
    font-family: "Vollkorn", serif; font-weight: 400;
    font-size: 20px; letter-spacing: 0.5px; margin-top: 46px;
  }
  .brand__tagline {
    font-family: "Open Sans", sans-serif; font-size: 11px;
    margin-top: 7px;
  }

  .person {
    position: absolute; left: 0; width: 321px; top: 274px;
    text-align: center;
  }
  .person__name {
    font-family: "Vollkorn", serif; font-weight: 500;
    font-size: 21px; color: var(--white); letter-spacing: 0.5px;
  }
  .person__role {
    font-family: "Vollkorn", serif; font-size: 12.5px; line-height: 18px;
    color: var(--rose-text); letter-spacing: 0.4px; margin-top: 2px;
  }

  .contacts { position: absolute; left: 57px; top: 372px; list-style: none; }
  .contacts__item {
    display: flex; align-items: flex-start;
    font-family: "Vollkorn", serif; font-size: 11.5px; line-height: 15px;
    color: var(--muted); margin-bottom: 14px;
  }
  .contacts__item--address { margin-bottom: 13px; }
  .contacts__icon {
    flex: none; width: 15px; height: 15px; margin-right: 8px;
    border-radius: 50%; background: var(--rose);
    display: flex; align-items: center; justify-content: center;
  }
</style>
</head>
<body>
  <article class="card">
    <div class="card__top">
      <svg width="321" height="260" viewBox="0 0 321 260">
        <defs>
          <linearGradient id="roseFill" x1="0" y1="1" x2="1" y2="0">
            <stop offset="0" stop-color="#d31f4b"/>
            <stop offset="1" stop-color="#eb6c8d"/>
          </linearGradient>
        </defs>
        <polygon points="0,0 321,0 321,257 135,215 0,257" fill="url(#roseFill)"/>
      </svg>
    </div>

    <header class="brand">
      <div class="brand__mark"></div>
      <div class="brand__name">LORABECKET</div>
      <div class="brand__tagline">Counseling, Psychotherapy &amp; Expressive Arts</div>
    </header>

    <section class="person">
      <h1 class="person__name">LORA BECKET</h1>
      <p class="person__role">COUNSELING, PSYCHOTHERAPY &amp;<br>EXPRESSIVE ARTS</p>
    </section>

    <ul class="contacts">
      <li class="contacts__item contacts__item--address">
        <span class="contacts__icon"><svg width="9" height="9" viewBox="0 0 10 10"><path d="M5 1 L9.5 5 H8 V9 H6 V6.5 H4 V9 H2 V5 H0.5 Z" fill="#fff"/></svg></span>
        <span>2914 Alderwood Avenue, Suite D<br>San Francisco, CA 94127</span>
      </li>
      <li class="contacts__item">
        <span class="contacts__icon"><svg width="9" height="9" viewBox="0 0 10 10"><path d="M2 1 L4 3 L3 4.3 Q4.5 6 5.7 7 L7 6 L9 8 L7.6 9.4 Q4 9 0.6 2.4 Z" fill="#fff"/></svg></span>
        <span>415.206.3791</span>
      </li>
      <li class="contacts__item">
        <span class="contacts__icon"><svg width="9" height="7" viewBox="0 0 10 8"><rect x="0.5" y="0.5" width="9" height="7" fill="#fff"/><path d="M0.5 0.8 L5 4.5 L9.5 0.8" fill="none" stroke="#dc2f58" stroke-width="1"/></svg></span>
        <span>lorajanebecket@meadowpost.net</span>
      </li>
      <li class="contacts__item">
        <span class="contacts__icon"><svg width="9" height="9" viewBox="0 0 10 10"><rect x="1" y="1" width="8" height="6" fill="#fff"/><rect x="4" y="7" width="2" height="1.5" fill="#fff"/><rect x="2.5" y="8.5" width="5" height="1" fill="#fff"/></svg></span>
        <span>www.lorabecketmft.com</span>
      </li>
      <li class="contacts__item">
        <span class="contacts__icon"><svg width="9" height="7" viewBox="0 0 10 8"><rect x="0.5" y="0.5" width="9" height="7" rx="1" fill="#fff"/><circle cx="3.2" cy="3.5" r="1.3" fill="#dc2f58"/><rect x="5.3" y="2.5" width="3" height="1" fill="#dc2f58"/><rect x="5.3" y="4.5" width="3" height="1" fill="#dc2f58"/></svg></span>
        <span>MFT License Number 48671</span>
      </li>
    </ul>
  </article>
</body>
</html>
```